Advertisement flyer (editable) and market report template in same style

Advertisement flyer (aka 1 page Media Kit) for us to sell advertising space on our website banner, harborlumenquay.com, and a market report template in the same style.
We would like to use colors that are used on our website. The flyer and market report template should be simple, and professional-looking. It should not look "old" or "boring". I've attached two drafts (1 each respectively), and our logo.

Target Market(s)

30-60 year old men but should look cool, new-aged, and fresh.

Industry/Entity Type

Shipping

Font styles to use
Serif

Requirements
Must have
• Editable layout so we can adjust text, numbers, and graphics on all. A fresh and new look. Colors per www.HarborLumenQuay.com website.
Should not have
• Boring layout and font

```html
<!DOCTYPE html>
<html lang="en">
<head>
<meta charset="utf-8">
<title>Harbor Lumen Quay – Market Report</title>
<link href="https://fonts.googleapis.com/css2?family=Roboto+Condensed:wght@300;400;700&display=swap" rel="stylesheet">
<style>
:root{
  --canvas:#e6e9ed;
  --brand:#1596e0;
  --brand-dark:#0f6aa6;
  --sea-top:#2c8fd2;
  --sea-mid:#1c6fa8;
  --ink:#15181c;
  --white:#ffffff;
  --panel:rgba(88,98,112,.82);
  --panel-line:rgba(255,255,255,.25);
  --vlcc:#1a9be6;
  --black-panel:rgba(10,12,14,.88);
  --footer:#0d0e10;
}
*{box-sizing:border-box;margin:0;padding:0}
html,body{width:1200px;height:1200px;overflow:hidden}
body{background:var(--canvas);font-family:"Roboto Condensed",sans-serif;color:var(--white);position:relative}

.page{position:absolute;overflow:hidden;box-shadow:0 6px 20px rgba(0,0,0,.25)}
.flyer{left:69px;top:122px;width:505px;height:652px;background:linear-gradient(180deg,var(--sea-top) 110px,var(--sea-mid) 320px,#235e86 420px)}
.report{left:623px;top:398px;width:510px;height:653px;background:linear-gradient(180deg,#cfe7f5 0,#6fb7e2 90px,#2d8cc9 260px,#1d6fa6 360px)}

.photo{position:absolute;left:0;right:0}
.flyer .photo{top:400px;bottom:66px;background:linear-gradient(180deg,rgba(35,94,134,0) 0,#3f6f86 20%,#7a6a58 55%,#5a3a2c 100%)}
.report .photo{top:370px;bottom:0;background:linear-gradient(180deg,rgba(29,111,166,0) 0,#4f7f92 20%,#8a5a3f 55%,#2d4f66 100%)}

.header{position:absolute;left:0;top:0;width:100%;height:150px}
.brand-name{position:absolute;left:26px;top:76px;font-size:17px;font-weight:700;color:var(--ink)}
.welcome{position:absolute;left:262px;top:34px;width:220px;text-align:center;color:var(--brand)}
.welcome .line1{font-size:22px;font-weight:300}
.welcome .line2{font-size:23px;font-weight:700;margin-top:2px}

.intro{position:absolute;left:37px;top:132px;width:432px;font-size:9px;line-height:11.5px;text-align:justify;font-weight:300}
.date-pill{position:absolute;left:147px;top:208px;width:210px;height:34px;background:var(--white);color:var(--ink);border-radius:8px;font-size:20px;text-align:center;line-height:34px}

.section-title{position:absolute;font-size:16px;font-weight:700;text-align:center;width:215px;letter-spacing:.3px}
.report .section-title{color:var(--ink)}
.report .section-title.light{color:var(--white)}

.rate-table{position:absolute;border-collapse:collapse;table-layout:fixed;background:var(--panel);font-size:10.5px}
.rate-table caption{font-size:15px;line-height:26px;background:var(--panel);text-transform:uppercase}
.rate-table th,.rate-table td{border:1px solid var(--panel-line);text-align:center;font-weight:400;height:22px;line-height:1}
.rate-table th small{font-size:8.5px;display:block}
.rate-table .up::after{content:" ↑";font-weight:700}
.rate-table .down::after{content:" ↓";font-weight:700}
.rate-table.vlcc{background:var(--vlcc);font-size:9.5px}
.rate-table.vlcc caption{background:var(--vlcc);line-height:23px;font-size:14px}
.rate-table.vlcc th,.rate-table.vlcc td{height:19px}
.rate-table.vlcc td:first-child{font-size:8.5px}
.rate-table.mrlr{font-size:9.5px}
.rate-table.mrlr caption{line-height:24px;font-size:14px}
.rate-table.mrlr th,.rate-table.mrlr td{height:19.5px}
.rate-table.bunker{background:var(--black-panel);font-size:9.5px}
.rate-table.bunker caption{background:var(--black-panel);line-height:24px;font-size:14px}
.rate-table.bunker th,.rate-table.bunker td{height:19px;border-color:rgba(255,255,255,.15)}

.note{position:absolute;background:var(--panel);font-size:9px;line-height:11.6px;font-weight:300;padding:10px 9px;text-align:justify}

.footer{position:absolute;left:0;bottom:0;width:100%;height:66px;background:var(--footer);font-size:9px;line-height:11.8px;font-weight:300}
.footer .col{position:absolute;top:9px;text-align:center}
.footer .divider{position:absolute;top:12px;width:1px;height:42px;background:rgba(255,255,255,.5)}

.chart{position:absolute;left:26px;top:198px;width:200px;height:138px}
</style>
</head>
<body>

<section class="page flyer">
  <div class="photo" role="img" aria-label="Aerial photograph of an industrial port coastline with cargo ships at the pier"></div>

  <svg class="header" viewBox="0 0 505 150" preserveAspectRatio="none" aria-hidden="true">
    <path d="M0 0H505V116C380 96 240 98 120 112C70 118 30 124 0 126Z" fill="#fff"/>
  </svg>
  <div class="brand-name">Harbor Lumen Quay</div>
  <div class="welcome">
    <div class="line1">Welcome to the</div>
    <div class="line2">Harbor Lumen Quay</div>
  </div>

  <p class="intro">Lorem Ipsum is simply dummy text of the printing and typesetting industry. Lorem Ipsum has been the industry's standard dummy text ever since the 1500s, when an unknown printer took a galley of type and scrambled it to make a type specimen book. It has survived not only five centuries, but also the leap into electronic typesetting, remaining essentially unchanged.</p>

  <div class="date-pill">SEPTEMBER 28, 2016</div>

  <h2 class="section-title" style="left:27px;top:265px">CRUDE</h2>
  <table class="rate-table" style="left:27px;top:288px;width:215px">
    <caption>Crude Prices</caption>
    <tr><th>$/bbl</th><th>22-Sep</th><th>15-Sep</th><th>w-o-w<small>change</small></th></tr>
    <tr><td>ICE Brent</td><td>47.29</td><td>46.30</td><td class="up">0.99</td></tr>
    <tr><td>Dtd Brent</td><td>47.29</td><td>46.30</td><td class="up">0.99</td></tr>
    <tr><td>Dubai</td><td>44.71</td><td>42.86</td><td class="up">1.85</td></tr>
  </table>
  <p class="note" style="left:262px;top:288px;width:216px;height:113px">Lorem Ipsum is simply dummy text of the printing and typesetting industry. Lorem Ipsum has been the industry's standard dummy text ever since the 1500s, when an unknown printer took a galley of type and scrambled it to make a type specimen book. It has survived not only five centuries, but also the leap into electronic typesetting, remaining essentially unchanged.</p>

  <h2 class="section-title" style="left:27px;top:423px">PRODUCTS</h2>
  <table class="rate-table" style="left:27px;top:446px;width:215px">
    <caption>Crude Prices</caption>
    <tr><th>$/bbl</th><th>22-Sep</th><th>15-Sep</th><th>w-o-w<small>change</small></th></tr>
    <tr><td>ICE Brent</td><td>47.29</td><td>46.30</td><td class="up">0.99</td></tr>
    <tr><td>Dtd Brent</td><td>47.29</td><td>46.30</td><td class="up">0.99</td></tr>
    <tr><td>Dubai</td><td>44.71</td><td>42.86</td><td class="up">1.85</td></tr>
  </table>
  <p class="note" style="left:262px;top:446px;width:216px;height:113px">Lorem Ipsum is simply dummy text of the printing and typesetting industry. Lorem Ipsum has been the industry's standard dummy text ever since the 1500s, when an unknown printer took a galley of type and scrambled it to make a type specimen book. It has survived not only five centuries, but also the leap into electronic typesetting, remaining essentially unchanged.</p>

  <footer class="footer">
    <div class="col" style="left:80px;width:160px;margin-left:-30px">Harbor Lumen Quay<br>48 Meridian Wharf #09-12<br>Singapore 039177</div>
    <div class="divider" style="left:189px"></div>
    <div class="col" style="left:192px;width:84px">PHONE<br>+65 6100 2350<br>+1-800-555-0142</div>
    <div class="divider" style="left:279px"></div>
    <div class="col" style="left:284px;width:160px">For General Inquiries<br>Contact@HarborLumenQuay.com<br>www.HarborLumenQuay.com</div>
  </footer>
</section>

<section class="page report">
  <div class="photo" role="img" aria-label="Aerial photograph of a port with ore stockpiles, piers and tankers at sea"></div>

  <h2 class="section-title" style="left:29px;top:26px;width:193px">VLCC</h2>
  <table class="rate-table vlcc" style="left:29px;top:48px;width:193px">
    <caption>Spot VLCC Rates</caption>
    <tr><th>WS</th><th>22-Sep</th><th>15-Sep</th><th>w-o-w<small>change</small></th></tr>
    <tr><td>AG/USGC</td><td>25.00</td><td>22.00</td><td class="up">3.00</td></tr>
    <tr><td>AG/Japan</td><td>38.00</td><td>32.00</td><td class="up">6.00</td></tr>
    <tr><td>AG<br>Singapore</td><td>39.00</td><td>33.00</td><td class="up">6.00</td></tr>
    <tr><td>WAF/USGC</td><td>42.50</td><td>45.00</td><td class="down">-2.50</td></tr>
    <tr><td>WAF/Far East</td><td>48.50</td><td>42.50</td><td class="up">6.00</td></tr>
  </table>

  <svg class="chart" viewBox="0 0 200 138" role="img" aria-label="Line chart of rates from January 2015 to July 2016">
    <g fill="#fff" font-family="Roboto Condensed, sans-serif" font-size="8.5">
      <text x="0" y="10">4.5</text><text x="0" y="23">4.0</text><text x="0" y="36">3.5</text>
      <text x="0" y="49">3.0</text><text x="0" y="61">2.5</text><text x="0" y="74">2.0</text>
      <text x="0" y="87">1.5</text><text x="0" y="100">1.0</text><text x="0" y="113">0.5</text>
      <text x="0" y="125">0.5</text>
    </g>
    <polyline fill="none" stroke="#fff" stroke-width="2" stroke-linejoin="round"
      points="24,100 27,92 30,96 33,88 36,94 39,70 42,84 45,76 48,90 51,72 54,82 57,60 60,66 63,44 66,52 69,34 72,46 75,78 78,70 81,90 84,84 87,100 90,88 93,98 96,92 99,104 102,86 105,96 108,80 111,98 114,84 117,104 120,94 123,112 126,100 129,108 132,96 135,106 138,110 141,112 144,104 147,118 150,114 153,120 156,112 159,122 162,114 165,120 168,108"/>
    <g fill="#1d5f8c" stroke="#fff" stroke-width=".5">
      <rect x="17" y="130" width="18" height="7"/><rect x="40" y="130" width="18" height="7"/>
      <rect x="63" y="130" width="18" height="7"/><rect x="86" y="130" width="18" height="7"/>
      <rect x="109" y="130" width="18" height="7"/><rect x="132" y="130" width="18" height="7"/>
      <rect x="155" y="130" width="18" height="7"/>
    </g>
    <g fill="#fff" font-family="Roboto Condensed, sans-serif" font-size="5.5" text-anchor="middle">
      <text x="26" y="135.5">Jan-15</text><text x="49" y="135.5">Apr-15</text><text x="72" y="135.5">Jul-15</text>
      <text x="95" y="135.5">Oct-15</text><text x="118" y="135.5">Jan-15</text><text x="141" y="135.5">Apr-15</text>
      <text x="164" y="135.5">Jul-15</text>
    </g>
  </svg>

  <p class="note" style="left:249px;top:30px;width:232px;height:304px;padding:24px 15px;line-height:11.7px">Lorem Ipsum is simply dummy text of the printing and typesetting industry. Lorem Ipsum has been the industry's standard dummy text ever since the 1500s, when an unknown printer took a galley of type and scrambled it to make a type specimen book. It has survived not only five centuries, but also the leap into electronic typesetting, remaining essentially unchanged. Lorem Ipsum is simply dummy text of the printing and typesetting industry. Lorem Ipsum has been the industry's standard dummy text ever since the 1500s, when an unknown printer took a galley of type and scrambled it to make a type specimen book. It has survived not only five centuries, but also the leap into electronic typesetting, remaining essentially unchanged. Lorem Ipsum is simply dummy text of the printing and typesetting industry. Lorem Ipsum has been the industry's standard dummy text ever since the 1500s, when an unknown printer took a galley of type and scrambled it to make a type specimen book. It has survived not only five centuries, but also the leap into electronic typesetting, remaining essentially unchanged.</p>

  <h2 class="section-title light" style="left:30px;top:347px;width:231px">MR/LR</h2>
  <table class="rate-table mrlr" style="left:30px;top:370px;width:231px">
    <col style="width:94px"><col><col><col>
    <caption>Spot MR/LR Rates</caption>
    <tr><th>WS</th><th>22-Sep</th><th>15-Sep</th><th>w-o-w<small>change</small></th></tr>
    <tr><td>AG/Japan (75 kt)</td><td>55.00</td><td>67.50</td><td>-12.50</td></tr>
    <tr><td>AG/Japan (55 kt)</td><td>80.00</td><td>82.50</td><td>-2.50</td></tr>
    <tr><td>AG/Japan (30 kt)</td><td>100.00</td><td>92.50</td><td>7.50</td></tr>
    <tr><td>Singapore/Japan (30 kt)</td><td>117.00</td><td>117.50</td><td>-0.50</td></tr>
  </table>
  <p class="note" style="left:272px;top:370px;width:209px;height:120px">Lorem Ipsum is simply dummy text of the printing and typesetting industry. Lorem Ipsum has been the industry's standard dummy text ever since the 1500s, when an unknown printer took a galley of type and scrambled it to make a type specimen book. It has survived not only five centuries, but also the leap into electronic typesetting, remaining essentially unchanged.</p>

  <h2 class="section-title light" style="left:30px;top:502px;width:231px">BUNKER</h2>
  <table class="rate-table bunker" style="left:30px;top:526px;width:231px">
    <col style="width:94px"><col><col><col>
    <caption>Bunker Prices</caption>
    <tr><th>$/T</th><th>22-Sep</th><th>15-Sep</th><th>w-o-w<small>change</small></th></tr>
    <tr><td>Singapore 380 cst</td><td>255.00</td><td>258.00</td><td>-3.00</td></tr>
    <tr><td>Singapore 180 cst</td><td>266.00</td><td>271.00</td><td>-5.00</td></tr>
    <tr><td>Gasoil</td><td>412.00</td><td>415.00</td><td>-3.00</td></tr>
  </table>
  <p class="note" style="left:272px;top:526px;width:209px;height:100px">Lorem Ipsum is simply dummy text of the printing and typesetting industry. Lorem Ipsum has been the industry's standard dummy text ever since the 1500s, when an unknown printer took a galley of type and scrambled it to make a type specimen book. It has survived not only five centuries, but also the leap into electronic typesetting, remaining essentially unchanged.</p>
</section>

</body>
</html>
```